Quorlapex

Hi everyone!

Looks like our project is more sophisticated than we expected. So good news - we increased the budget! and one of you will sure get the prize - no money back for us!

We are a young Russian company that specializes in in-taxi entertainment. We believe that our key strength is great attention to user experience. We've devoted much effort to improve ergonomics of our devices - tablet PCs that we install in the taxis. And yes, we enjoy to simplify things!

Now we need the most basic things - a logo and some staff for client meetings (primarily advertisers and ad agencies).

As for logo - we already have one engraved on the prototypes of our device (see attached file). This is one of the ideas (still far from perfect) - what we appreciate in it is minimalistic yet stylish approach.

As for "take it to the meeting stuff" we want to start with name card, pen and notepad (A4) that we will leave in clients's office, also as a reminder. Shall your have more smart ideas - always welcome!

As for logo and name cards - we would like to make an image of serious but modern company. Our design should communicate creativity and reliability. We believe that "to understand is to simplify" - minimalistic design is the most difficult one. Its better to work hard on fonts and arrangement, than put 10 variegated images.

SO THE TASK IS TO DESIGN:
- a logo
- a name card
- a note pad (great example in attachment)
- a pen

Shall you have more questions - please ask in comments.

We look forward to meeting like-minded fellows here!

Target Market(s)

Out target are:

- advertiser
- advertising agencies
- taxi passenger

Industry/Entity Type

It Company

Requirements
Must have
• font should be chosen very carefully
Nice to have
• classic minimalistic plain text only but very stylish name card is a dream of one of our co-founders:)
Should not have
• we do not want to have taxi-like colors and chess-boards. We are closer to "innovation", "entertainment", and "user experience", rather than "taxi".

```html
<!DOCTYPE html>
<html lang="en">
<head>
<meta charset="utf-8">
<title>Quorlapex letterheads</title>
<link rel="stylesheet" href="https://fonts.googleapis.com/css2?family=Arimo:wght@400;700&display=swap">
<style>
  :root {
    --backdrop: #2288bd;
    --paper: #e7e7e6;
    --brand-blue: #2f4c9c;
    --band-dark: #1e3366;
    --band-light: #4a64a8;
    --white: #ffffff;
  }
  * { margin: 0; padding: 0; box-sizing: border-box; }
  html, body {
    width: 1200px;
    height: 1000px;
    overflow: hidden;
    background: var(--backdrop);
    font-family: "Arimo", Arial, sans-serif;
  }
  .canvas {
    position: relative;
    width: 1200px;
    height: 1000px;
  }
  .letterhead {
    position: absolute;
    top: 115px;
    width: 530px;
    height: 750px;
    background: var(--paper);
    overflow: hidden;
  }
  .letterhead--plain { left: 42px; }
  .letterhead--banded { left: 623px; }

  .wordmark {
    position: absolute;
    font-weight: 700;
    font-size: 34px;
    letter-spacing: -1.4px;
    color: var(--brand-blue);
    line-height: 1;
  }
  .letterhead--plain .wordmark { left: 27px; top: 34px; }
  .letterhead--banded .wordmark { left: 23px; top: 44px; }

  .contacts {
    position: absolute;
    font-weight: 700;
    font-size: 9.5px;
    line-height: 10.6px;
    color: var(--brand-blue);
    list-style: none;
  }
  .letterhead--plain .contacts { left: 29px; top: 685px; }

  .footer-band {
    position: absolute;
    left: 0;
    bottom: 0;
    width: 100%;
    height: 70px;
  }
  .footer-band__photo {
    position: absolute;
    inset: 0;
    background: linear-gradient(100deg, var(--band-dark) 0%, var(--band-light) 45%, #6077b5 70%, var(--band-dark) 100%);
  }
  .footer-band .contacts {
    left: 29px;
    top: 12px;
    color: var(--white);
  }
</style>
</head>
<body>
<main class="canvas">
  <section class="letterhead letterhead--plain" aria-label="Letterhead, plain version">
    <div class="wordmark">quorlapex</div>
    <ul class="contacts">
      <li>654321, Kestrova, Verbenova str., 8-3</li>
      <li>Phone</li>
      <li>www.quorlapex.com</li>
      <li>mail@quorlapex.com</li>
    </ul>
  </section>

  <section class="letterhead letterhead--banded" aria-label="Letterhead, photo band version">
    <div class="wordmark">quorlapex</div>
    <div class="footer-band">
      <div class="footer-band__photo" role="img" aria-label="Blue-toned photograph of parked taxi cars"></div>
      <ul class="contacts">
        <li>654321, Kestrova, Verbenova str., 8-3</li>
        <li>Phone</li>
        <li>www.quorlapex.com</li>
        <li>mail@quorlapex.com</li>
      </ul>
    </div>
  </section>
</main>
</body>
</html>
```